New Company Business Card Design

I have a new company logo and I want a new business card design. I dont know if the logo file i attached is in the correct format or quality. We are a New York City Specialty construction Firm specializing in high risk out of the box projects. I want a simple and classy business card that people will his card is as crisp as the work his company does.

Target Market(s)

Clients in the heavy construction industry in New York City

Industry/Entity Type

Construction Company

Contact Information for Business Card

Simple Classy - DIFFERENT

Font styles to use
Other font styles liked:
• Mach the logo font in some way

Colors

Designer to choose colors to be used in the design.

Requirements
Must have
• Uniqueness
Nice to have
• Nothing particular - Just different and classy - Timeless
Should not have
• Goofy Shit or Gimmicky shit

```html
<!DOCTYPE html>
<html lang="en">
<head>
<meta charset="utf-8">
<title>Bramlet Associates – Business Card</title>
<link href="https://fonts.googleapis.com/css2?family=Roboto:wght@400;500;700;900&display=swap" rel="stylesheet">
<style>
  :root {
    --page-bg: #e9e7e4;
    --card-white: #ffffff;
    --ink: #111111;
    --brand-blue: #1b6fc2;
    --band-dark: #1c4a8f;
    --band-light: #1ea0df;
    --ring-blue: #1a9ae0;
    --black-bar: #000000;
    --back-dark: #0b0b0b;
    --back-mid: #262626;
    --white: #ffffff;
    --divider: #333333;
  }
  * { margin: 0; padding: 0; box-sizing: border-box; }
  html, body {
    width: 900px; height: 1200px; overflow: hidden;
    background: var(--page-bg);
    font-family: "Roboto", Arial, sans-serif;
  }
  .canvas { position: relative; width: 900px; height: 1200px; }

  .card {
    position: absolute; left: 97px; width: 700px; height: 408px;
    box-shadow: 0 6px 14px rgba(0,0,0,.25);
    overflow: hidden;
  }

  /* Front */
  .card-front { top: 172px; background: var(--card-white); }
  .wordmark {
    position: absolute; left: 0; right: 0; top: 88px;
    text-align: center; color: var(--brand-blue);
    font-weight: 900; line-height: 1;
  }
  .wordmark-name { display: block; font-size: 64px; letter-spacing: 2px; }
  .wordmark-sub { display: block; font-size: 22px; letter-spacing: 6px; margin-top: 10px; }

  .name-band {
    position: absolute; left: 0; right: 0; top: 225px; height: 27px;
    background: linear-gradient(90deg, var(--band-dark) 0%, var(--band-dark) 30%, var(--band-light) 85%);
    color: var(--white); font-weight: 700; font-size: 18px; letter-spacing: .5px;
    text-align: center; line-height: 27px;
  }

  .contact-row { position: absolute; left: 0; right: 0; top: 278px; height: 80px; }
  .contact-item {
    position: absolute; top: 0; width: 160px; margin-left: -80px;
    text-align: center; color: var(--ink); font-size: 17px;
  }
  .contact-item.small { font-size: 15px; top: 3px; }
  .contact-icon { display: block; margin: 0 auto 10px; width: 42px; height: 42px; }
  .contact-item.small .contact-icon { margin-bottom: 12px; }
  .divider {
    position: absolute; top: 278px; width: 1px; height: 70px; background: var(--divider);
  }

  .address-bar {
    position: absolute; left: 0; right: 0; bottom: 0; height: 40px;
    background: var(--black-bar); color: var(--white);
    font-size: 15px; text-align: center; line-height: 40px;
  }

  /* Back */
  .card-back {
    top: 652px;
    background: linear-gradient(90deg, var(--back-dark) 0%, var(--back-mid) 100%);
  }
  .card-back .wordmark { top: 148px; }
  .back-url {
    position: absolute; left: 0; right: 0; top: 350px;
    text-align: center; color: var(--white);
    font-weight: 700; font-size: 17px; letter-spacing: 2px;
  }
</style>
</head>
<body>
<main class="canvas">

  <section class="card card-front" aria-label="Business card front">
    <div class="wordmark">
      <span class="wordmark-name">BRAMLET</span>
      <span class="wordmark-sub">ASSOCIATES, INC.</span>
    </div>

    <div class="name-band">MARCUS T. RINALDI</div>

    <div class="contact-row">
      <div class="contact-item" style="left:108px">
        <svg class="contact-icon" viewBox="0 0 42 42" aria-hidden="true">
          <circle cx="21" cy="21" r="19" fill="var(--ink)" stroke="var(--ring-blue)" stroke-width="3"/>
          <rect x="15" y="11" width="12" height="20" rx="2" fill="none" stroke="#fff" stroke-width="2"/>
          <rect x="17.5" y="14" width="7" height="5" fill="#fff"/>
          <rect x="17.5" y="21" width="7" height="7" fill="#fff" opacity=".8"/>
        </svg>
        917-555-0143
      </div>
      <div class="contact-item" style="left:266px">
        <svg class="contact-icon" viewBox="0 0 42 42" aria-hidden="true">
          <circle cx="21" cy="21" r="19" fill="var(--ink)" stroke="var(--ring-blue)" stroke-width="3"/>
          <path d="M14 12 l4 -1 l2.5 5.5 l-2.5 2 q2 4.5 6 6.5 l2 -2.5 l5.5 2.5 l-1 4 q-9 1 -15 -7 q-3.5 -4.5 -1.5 -10z" fill="#fff"/>
        </svg>
        908-555-0118
      </div>
      <div class="contact-item small" style="left:423px">
        <svg class="contact-icon" viewBox="0 0 42 42" aria-hidden="true">
          <circle cx="21" cy="21" r="19" fill="var(--ink)" stroke="var(--ring-blue)" stroke-width="3"/>
          <g fill="none" stroke="#fff" stroke-width="1.6">
            <circle cx="21" cy="21" r="9"/>
            <ellipse cx="21" cy="21" rx="4" ry="9"/>
            <line x1="12" y1="21" x2="30" y2="21"/>
            <line x1="13.5" y1="16.5" x2="28.5" y2="16.5"/>
            <line x1="13.5" y1="25.5" x2="28.5" y2="25.5"/>
          </g>
        </svg>
        BRAMLET.COM
      </div>
      <div class="contact-item small" style="left:581px">
        <svg class="contact-icon" viewBox="0 0 42 42" aria-hidden="true">
          <circle cx="21" cy="21" r="19" fill="var(--ink)" stroke="var(--ring-blue)" stroke-width="3"/>
          <rect x="12" y="14" width="18" height="13" fill="#fff"/>
          <path d="M12 14 l9 7.5 l9 -7.5" fill="none" stroke="var(--ink)" stroke-width="1.6"/>
        </svg>
        MARC@BRAMLET.COM
      </div>
    </div>

    <span class="divider" style="left:187px"></span>
    <span class="divider" style="left:355px"></span>
    <span class="divider" style="left:490px"></span>

    <div class="address-bar">118 Harbor View Road - Linden, New Jersey 07036</div>
  </section>

  <section class="card card-back" aria-label="Business card back">
    <div class="wordmark">
      <span class="wordmark-name">BRAMLET</span>
      <span class="wordmark-sub">ASSOCIATES, INC.</span>
    </div>
    <div class="back-url">BRAMLET.COM</div>
  </section>

</main>
</body>
</html>
```